Harborline Ventures

I provide collision estimating for autobody shops, so when they need a collision estimate and they are too busy or don't have the software, i write that estimate for them. I do this either in person or virtual. I need a postcard mailer design, 6.25 x 9 inches, with a header that reads HARBORLINE VENTURES, highlighting 20+ years of experience, and text that reads ASK ABOUT OUR TRAINING

Target Market(s)

Autobody Repair shops

Industry/Entity Type

Autobody

```html
<!DOCTYPE html>
<html lang="en">
<head>
<meta charset="utf-8">
<title>Harborline Ventures – Postcard Mailer</title>
<link rel="stylesheet" href="https://fonts.googleapis.com/css2?family=Cabin:ital,wght@0,400;0,600;1,400&display=swap">
<style>
  :root {
    --bg: #231d12;
    --ink: #ffffff;
    --accent: #f04e23;
    --frame: #9a8a6c;
    --photo-red: #8e1f2a;
    --photo-dark: #3a2a28;
    --photo-gravel: #a8a49a;
  }
  html, body {
    margin: 0;
    padding: 0;
    width: 1200px;
    height: 833px;
    overflow: hidden;
    background: var(--bg);
  }
  .postcard {
    position: relative;
    width: 1200px;
    height: 833px;
    background: var(--bg);
    font-family: "Cabin", "Candara", sans-serif;
    color: var(--ink);
  }
  .info {
    position: absolute;
    left: 40px;
    width: 552px;
    top: 0;
    height: 833px;
    text-align: center;
  }
  .info p { margin: 0; position: absolute; left: 0; right: 0; white-space: nowrap; }
  .brand-name {
    top: 148px;
    font-size: 40px;
    line-height: 46px;
    font-weight: 600;
    letter-spacing: 1.5px;
    color: var(--accent);
  }
  .headline {
    top: 302px;
    font-size: 53px;
    line-height: 56px;
    font-weight: 600;
    letter-spacing: -0.5px;
  }
  .experience {
    top: 386px;
    font-size: 37px;
    font-weight: 600;
    line-height: 43px;
  }
  .experience .years { color: var(--accent); }
  .training {
    top: 481px;
    font-size: 33px;
    line-height: 38px;
    font-style: italic;
    font-weight: 400;
  }
  .website {
    top: 555px;
    font-size: 22px;
    line-height: 26px;
    font-weight: 600;
  }
  .contact {
    top: 613px;
    font-size: 24px;
    font-weight: 400;
    line-height: 35px;
    letter-spacing: 0.5px;
  }
  .photo-frame {
    position: absolute;
    left: 638px;
    top: 34px;
    width: 522px;
    height: 759px;
    border: 3px solid var(--frame);
    background:
      linear-gradient(160deg, #c9c4b8 0%, #c9c4b8 8%, transparent 14%),
      linear-gradient(200deg, transparent 55%, var(--photo-gravel) 75%),
      linear-gradient(135deg, var(--photo-dark) 0%, var(--photo-red) 35%, #b0323c 55%, var(--photo-red) 70%, #5a4a44 100%);
  }
</style>
</head>
<body>
  <main class="postcard">
    <section class="info">
      <p class="brand-name">HARBORLINE VENTURES</p>
      <p class="headline">Harborline Ventures</p>
      <p class="experience">More than <span class="years">20+</span> years<br>of estimating experience</p>
      <p class="training">Ask about our training</p>
      <p class="website">https://www.harborlineventures.com/</p>
      <p class="contact">Contact us:<br>(555) 214-7390<br>hello@harborlineventures.com</p>
    </section>
    <div class="photo-frame" role="img" aria-label="Photo of a red sedan with heavy collision damage along its front door and fender, parked on gravel"></div>
  </main>
</body>
</html>
```